Professionelles Webdesign für hochwertiges Coaching Business
Zielgruppe
Es geht um eine Coaching-Firma für Einzelcoaching, Team-Coaching in Firmen und Ausbildungen. Inhalt sind Kommunikation, Stressmanagement und Leistungssteigerung, Persönlichkeitsentwicklung bis hin zum Marketing für Coaches.
Aufgabenstellung
- siehe Briefing im Dateiupload
- Umsetzung via Baukastensystem. Wichtig ist, dass die Features mit dem Baukastensystem umsetzbar sind.
- Es dürfen bitte diese 4 Seiten gestaltet werden:
Startseite
Coaching
Training
Ausbildung
- Obgleich ich Kundenfokus auf der Website bevorzuge, darf sie mich auch etwas widerspiegeln. Für einen Eindruck über mich sind zwei Bilder dem Anhang beigefügt. Diese Bilder sollen NICHT in die Website eingebunden werden.

```html
<!DOCTYPE html>
<html lang="de">
<head>
<meta charset="utf-8">
<title>Falkenrath – Coaching für ein erfülltes Leben</title>
<link href="https://fonts.googleapis.com/css2?family=Poppins:wght@300;400;500;600;700;800&display=swap" rel="stylesheet">
<style>
:root{
  --red:#9b1c2e;
  --red-dark:#7d1524;
  --blue:#3b86d6;
  --ink:#1b1b1b;
  --muted:#7a7a7a;
  --light:#f4f4f4;
  --field:#f1f1f3;
  --white:#ffffff;
}
*{margin:0;padding:0;box-sizing:border-box}
html,body{width:1200px;height:4197px;overflow:hidden}
body{font-family:'Poppins',sans-serif;color:var(--ink);background:var(--white);position:relative}
.abs{position:absolute}

/* hero */
.hero{position:absolute;left:0;top:0;width:1200px;height:602px;background:var(--red);overflow:hidden}
.hero-photo{position:absolute;right:0;top:0;width:760px;height:602px;background:radial-gradient(ellipse at 65% 35%,#c2475a 0%,#a82538 45%,var(--red) 80%)}
.brand{position:absolute;display:flex;align-items:center;gap:12px;color:var(--white)}
.brand-dot{width:40px;height:40px;border-radius:50%;border:3px solid var(--white)}
.brand-name{font-weight:600;font-size:24px;letter-spacing:1px}
.lang{position:absolute;left:977px;top:37px;width:117px;height:43px;border:2px solid var(--white);border-radius:6px;color:var(--white);font-size:12px;display:flex;align-items:center;padding:0 14px;gap:10px}
.hero-kicker{position:absolute;left:106px;top:268px;color:var(--white);font-size:21px;font-weight:300}
.hero-title{position:absolute;left:104px;top:290px;color:var(--white);font-size:60px;font-weight:800;letter-spacing:-.5px}
.hero-btn{position:absolute;top:409px;width:234px;height:60px;background:var(--white);border-radius:4px;display:flex;align-items:center;justify-content:space-between;padding:0 28px;color:var(--red);font-size:15px;font-weight:500}

/* welcome */
.welcome-title{position:absolute;left:106px;top:682px;font-size:36px;font-weight:800}
.welcome-text{position:absolute;left:106px;top:740px;width:435px;font-size:11.5px;line-height:18.5px;color:var(--muted)}
.welcome-text p{margin-bottom:18px}
.welcome-text b{color:#333;font-weight:600}
.welcome-tag{position:absolute;left:106px;top:1017px;font-size:15px;font-weight:600;color:#555}
.btn-blue{position:absolute;background:var(--blue);color:var(--white);border-radius:5px;display:flex;align-items:center;justify-content:center;font-size:14px;font-weight:600}
.feature{position:absolute;width:240px;text-align:center;font-size:12px;line-height:18px;color:#444}
.feature b{font-weight:600;color:var(--ink)}
.feature svg{display:block;margin:0 auto 10px}

/* testimonials */
.testimonials{position:absolute;left:0;top:1213px;width:1200px;height:651px;background:var(--red);color:var(--white)}
.t-kicker{position:absolute;left:0;width:1200px;top:58px;text-align:center;font-size:22px;font-weight:300}
.t-title{position:absolute;left:0;width:1200px;top:82px;text-align:center;font-size:58px;font-weight:800}
.t-card{position:absolute;width:320px;text-align:center}
.t-photo{width:190px;height:190px;border-radius:50%;border:4px solid var(--white);margin:0 auto 30px;background:radial-gradient(circle at 50% 40%,#c9a98f,#6e5a4e)}
.t-quote{font-size:16px;line-height:24px;font-weight:300}
.t-name{font-size:12px;font-weight:600;margin-top:16px}

/* offers */
.diamond{position:absolute;width:287px;height:287px;transform:rotate(45deg) scale(.72);border-radius:60px}
.offer-title{position:absolute;font-size:28px;font-weight:800}
.offer-text{position:absolute;width:440px;font-size:11.5px;line-height:18.5px;color:var(--muted)}
.offer-text p{margin-bottom:18px}

/* business */
.business{position:absolute;left:0;top:2564px;width:1200px;height:350px;background:var(--light)}
.business-photo{position:absolute;left:0;top:0;width:600px;height:350px;background:linear-gradient(90deg,#6f7a7a 0%,#9aa39e 45%,rgba(244,244,244,0) 100%)}

/* partners */
.partner{position:absolute;top:2998px;display:flex;align-items:center;gap:10px;font-size:22px;font-weight:600;color:#3f4452}
.partner i{width:30px;height:30px;border-radius:50%;background:#3f4452;display:block}

/* contact */
.footer-band{position:absolute;left:0;top:3635px;width:1200px;height:562px;background:var(--red)}
.contact-card{position:absolute;left:106px;top:3134px;width:985px;height:573px;background:var(--white);border-radius:30px;overflow:hidden;box-shadow:0 20px 60px rgba(0,0,0,.08)}
.map{position:absolute;left:0;top:0;width:467px;height:573px;background:linear-gradient(135deg,#e6e8ec,#d9dde3)}
.c-kicker{position:absolute;left:532px;top:38px;font-size:19px;font-weight:300}
.c-title{position:absolute;left:532px;top:62px;font-size:30px;font-weight:800}
.c-info{position:absolute;top:142px;font-size:12px;font-weight:600;color:var(--red)}
.c-info svg{display:block;margin-bottom:6px}
.field{position:absolute;left:532px;width:402px;height:36px;background:var(--field);border-radius:8px;font-size:10px;color:#b5b5b5;padding:11px 20px}

/* footer */
.f-col{position:absolute;top:3886px;color:var(--white)}
.f-col h4{font-size:15px;font-weight:600;margin-bottom:20px}
.f-col li{list-style:none;font-size:11.5px;line-height:24px}
.social{position:absolute;top:4116px;left:0;width:1200px;display:flex;justify-content:center;gap:14px}
.social i{width:22px;height:22px;border-radius:50%;background:var(--white);display:block}
.copyright{position:absolute;left:0;width:1200px;top:4152px;text-align:center;font-size:11px;color:var(--white)}
</style>
</head>
<body>

<section class="hero">
  <div class="hero-photo" role="img" aria-label="Lachende junge Frau mit langen Haaren, rot eingefärbtes Foto"></div>
  <div class="brand" style="left:106px;top:30px"><span class="brand-dot"></span><span class="brand-name">FALKENRATH</span></div>
  <div class="lang">
    <svg width="18" height="18" viewBox="0 0 18 18" fill="none" stroke="#fff" stroke-width="1.4"><circle cx="9" cy="9" r="7.5"/><path d="M1.5 9h15M9 1.5c2.5 2.5 2.5 12.5 0 15M9 1.5c-2.5 2.5-2.5 12.5 0 15"/></svg>
    <span>De</span>
    <svg style="margin-left:auto" width="10" height="6" viewBox="0 0 10 6"><path d="M1 1l4 4 4-4" stroke="#fff" stroke-width="1.5" fill="none"/></svg>
  </div>
  <p class="hero-kicker">Coaching für ein</p>
  <h1 class="hero-title">Erfülltes Leben</h1>
  <a class="hero-btn" style="left:106px">Für Einzelpersonen <svg width="16" height="16" viewBox="0 0 16 16"><path d="M3 13L13 3M5 3h8v8" stroke="#9b1c2e" stroke-width="2" fill="none"/></svg></a>
  <a class="hero-btn" style="left:375px">Für Firmen <svg width="16" height="16" viewBox="0 0 16 16"><path d="M3 13L13 3M5 3h8v8" stroke="#9b1c2e" stroke-width="2" fill="none"/></svg></a>
</section>

<section class="welcome">
  <h2 class="welcome-title">Willkommen</h2>
  <div class="welcome-text">
    <p><b>Hedwig</b> ist eine erfahrene Coach, die sich auf die Coaching von anderen Coaches spezialisiert hat. Sie hat über 20 Jahre Erfahrung in der Coaching-Branche und hat hunderten Coaches dabei geholfen, <b>ihre Fähigkeiten zu verbessern und effektiver zu werden.</b></p>
    <p>Wenn Sie ein Coach sind, der Ihre Fähigkeiten verbessern möchte, dann ist Hedwig die perfekte Coach für Sie. Sie wird Ihnen helfen, Ihre Coaching-Fähigkeiten zu entwickeln, in Ihren Coaching-Sitzungen effektiver zu werden und ein erfolgreiches Coaching-Business aufzubauen.</p>
    <p>Wenn Sie ein Coach sind, der Hilfe sucht, um Ihre Fähigkeiten zu verbessern, ein erfolgreiches Coaching-Business aufzubauen oder sich in einem bestimmten Bereich zu spezialisieren, dann kontaktieren Sie Hedwig noch heute. Sie wird Ihnen gerne dabei helfen, Ihre Ziele zu erreichen.</p>
  </div>
  <p class="welcome-tag">Willkommen auf der nächsten Ebene des Coachings!</p>
  <a class="btn-blue" style="left:106px;top:1079px;width:151px;height:44px">Kontakt</a>

  <div class="feature" style="left:682px;top:740px">
    <svg width="80" height="72" viewBox="0 0 80 72" fill="none" stroke="#3b86d6" stroke-width="2"><circle cx="54" cy="22" r="16"/><path d="M8 64l20-14 10 6 12-18M6 68h40"/></svg>
    <b>Herausforderungen</b> meistern
  </div>
  <div class="feature" style="left:902px;top:740px">
    <svg width="80" height="72" viewBox="0 0 80 72" fill="none" stroke="#3b86d6" stroke-width="2"><circle cx="40" cy="26" r="12"/><path d="M34 40h12v8H34zM40 6v6M22 26h-6M64 26h-6M27 13l-4-4M53 13l4-4"/></svg>
    <b>Klarer Blick</b><br>auf die Situation
  </div>
  <div class="feature" style="left:682px;top:928px">
    <svg width="80" height="72" viewBox="0 0 80 72" fill="none" stroke="#3b86d6" stroke-width="2"><circle cx="40" cy="34" r="26"/><path d="M40 8v52M22 20c8 6 8 22 0 28M58 20c-8 6-8 22 0 28"/></svg>
    <b>Wissenschaftlich fundierte Methoden</b><br>basierend auf der<br>Neurobiologie
  </div>
  <div class="feature" style="left:902px;top:928px">
    <svg width="80" height="72" viewBox="0 0 80 72" fill="none" stroke="#3b86d6" stroke-width="2"><circle cx="40" cy="38" r="26"/><circle cx="40" cy="38" r="16"/><circle cx="40" cy="38" r="5"/><path d="M40 4v14M40 58v14M6 38h14M60 38h14"/></svg>
    <b>Punktgenau &amp; beweisen</b><br>nachhaltig wirksam
  </div>
</section>

<section class="testimonials">
  <p class="t-kicker">Unsere Kunden sind</p>
  <h2 class="t-title">Begeistert!</h2>
  <div class="t-card" style="left:74px;top:242px">
    <div class="t-photo" role="img" aria-label="Porträtfoto einer lachenden blonden Kundin"></div>
    <p class="t-quote">"Mit dem Coaching habe ich meine Ziele erreicht."</p>
    <p class="t-name">Lena Vogt</p>
  </div>
  <div class="t-card" style="left:439px;top:242px">
    <div class="t-photo" role="img" aria-label="Porträtfoto eines Kunden im hellen Anzug"></div>
    <p class="t-quote">"Nach dem Coaching bin ich stressfrei und leistungsstark."</p>
    <p class="t-name">Jonas Brandt</p>
  </div>
  <div class="t-card" style="left:799px;top:242px">
    <div class="t-photo" role="img" aria-label="Porträtfoto einer Kundin am Schreibtisch"></div>
    <p class="t-quote">"Mein Coach hat mir geholfen, meine Kommunikationsfähigkeiten zu verbessern."</p>
    <p class="t-name">Mira Keller</p>
  </div>
</section>

<section class="offers">
  <div class="diamond" style="left:75px;top:1925px;background:linear-gradient(135deg,#e0a21a,#8a5a08)" role="img" aria-label="Frau genießt die Sonne im Feld, gelb getönt"></div>
  <div class="diamond" style="left:681px;top:1925px;background:linear-gradient(135deg,#2fae5a,#0d4a24)" role="img" aria-label="Zwei lachende Frauen, grün getönt"></div>
  <h3 class="offer-title" style="left:106px;top:2235px">Life Coaching</h3>
  <div class="offer-text" style="left:106px;top:2292px">
    <p>Im Life Coaching klären wir, was Ihnen wirklich wichtig ist. Gemeinsam entwickeln wir Schritte, die zu Ihrem Alltag passen, und stärken Ihre innere Ruhe. Sie lernen, Belastungen früh zu erkennen, Grenzen klar zu setzen und Entscheidungen mit Zuversicht zu treffen. So entsteht Raum für Energie, Freude und neue Perspektiven.</p>
    <p>Jede Sitzung richtet sich nach Ihrem Tempo. Wir arbeiten lösungsorientiert, mit bewährten Methoden und viel Vertrauen, damit Veränderungen nachhaltig bleiben.</p>
  </div>
  <h3 class="offer-title" style="left:677px;top:2235px">Ausbildung</h3>
  <div class="offer-text" style="left:677px;top:2292px">
    <p>Unsere Ausbildung richtet sich an angehende Coaches, die fundiertes Wissen und praktische Sicherheit suchen. Sie lernen Gesprächsführung, Methodik und den Aufbau eines eigenen Coaching-Business. In kleinen Gruppen üben Sie an echten Fällen und erhalten persönliches Feedback für Ihren Weg.</p>
  </div>
</section>

<section class="business">
  <div class="business-photo" role="img" aria-label="Gruppe junger Menschen beim High Five im Freien"></div>
  <h3 class="offer-title" style="left:677px;top:60px">Business Coaching</h3>
  <div class="offer-text" style="left:677px;top:116px;width:390px">
    <p>Im Business Coaching stärken wir Teams und Führungskräfte. Wir verbessern Kommunikation, senken Stress und steigern die Leistung im Arbeitsalltag. Workshops und Einzelsitzungen werden passend zu Ihrem Unternehmen gestaltet.</p>
    <p>Sprechen Sie uns an und wir entwickeln gemeinsam Ihr Programm.</p>
  </div>
</section>

<section class="partners">
  <div class="partner" style="left:106px"><i></i>Nordwerk</div>
  <div class="partner" style="left:264px"><i></i>Kaltera</div>
  <div class="partner" style="left:494px"><i></i>Brivon</div>
  <div class="partner" style="left:727px"><i></i>Solmaro</div>
  <div class="partner" style="left:936px"><i></i>Quentis</div>
</section>

<div class="footer-band"></div>
<section class="contact-card">
  <div class="map" role="img" aria-label="Karte mit dem Standort des Coaching-Studios"></div>
  <p class="c-kicker">Wir freuen uns,</p>
  <h2 class="c-title">von Ihnen zu hören!</h2>
  <div class="c-info" style="left:532px">
    <svg width="22" height="20" viewBox="0 0 22 20" fill="none" stroke="#9b1c2e" stroke-width="1.5"><path d="M4 2l4 1 1 4-2 2c1 3 3 5 6 6l2-2 4 1 1 4c-9 1-17-7-16-16z"/></svg>
    +41 032 555 01 27
  </div>
  <div class="c-info" style="left:740px">
    <svg width="24" height="20" viewBox="0 0 24 20" fill="none" stroke="#9b1c2e" stroke-width="1.5"><rect x="2" y="3" width="20" height="14"/><path d="M2 3l10 8 10-8"/></svg>
    info@falkenrath-training.com
  </div>
  <div class="field" style="top:194px">Name</div>
  <div class="field" style="top:249px">E-Mail Adresse</div>
  <div class="field" style="top:304px">Telefonnummer</div>
  <div class="field" style="top:358px;height:95px">Nachricht</div>
  <a class="btn-blue" style="left:532px;top:488px;width:152px;height:44px">Senden</a>
</section>

<footer>
  <div class="brand" style="left:470px;top:3782px"><span class="brand-dot"></span><span class="brand-name">FALKENRATH</span></div>
  <div class="f-col" style="left:114px"><h4>Coaching</h4><ul><li>Beziehungscoaching</li><li>Gesundheitscoaching</li><li>Stressmanagement</li><li>Persönlichkeitsentwicklung</li><li>Performancecoaching</li></ul></div>
  <div class="f-col" style="left:386px"><h4>Training</h4><ul><li>Kommunikationstraining</li><li>Sales Training</li><li>Training zu Work-Health-Balance</li></ul></div>
  <div class="f-col" style="left:707px"><h4>Über uns</h4><ul><li>Das Unternehmen</li><li>Über Hedwig Falkenrath</li><li>Kontakt</li><li>Nachrichten</li></ul></div>
  <div class="f-col" style="left:987px"><h4>Informationen</h4><ul><li>AGB</li><li>Impressum</li><li>Datenschutz</li></ul></div>
  <div class="social"><i></i><i></i><i></i></div>
  <p class="copyright">© 2023 falkenrath-training.com, Alle Richten sind behalten.</p>
</footer>

</body>
</html>
```